Flyer Design Project with menu

We are from Juniper Table Restaurant. We usually serve breakfast, soul food, fried and BBQ Ribs , legs, wings etc. We located at 2873 n. Willow avenue, canton, 39046, MS. Since this is a new restaurant we want to let people know about us. Please create a good professional flyer including menu on that. Thank you. Please let us know if you need any other information.
Updates

Target Market(s)

We want to attract customers from 3 different locations near 15 miles radius.

Industry/Entity Type

American Restaurant

Font styles to use
Serif

Requirements
Must have
• Good graphics with food pictures.
• Soul food graphic pictures, RIBS, FISH and breakfast regular.
Nice to have
• 20% discount coupon offer.

```html
<!DOCTYPE html>
<html lang="en">
<head>
<meta charset="utf-8">
<title>Juniper Table Restaurant – Menu</title>
<link href="https://fonts.googleapis.com/css2?family=Teko:wght@500;600&family=Open+Sans:ital,wght@0,400;0,600;1,400&display=swap" rel="stylesheet">
<style>
  :root{
    --ink:#3b1c16;
    --paper:#ffffff;
    --backdrop:#d9d9d9;
    --rule:#555555;
  }
  html,body{margin:0;padding:0;overflow:hidden;}
  body{width:1200px;height:960px;background:var(--backdrop);position:relative;font-family:"Open Sans",sans-serif;color:var(--ink);}
  .menu-page{position:absolute;left:230px;top:15px;width:740px;height:930px;background:var(--paper);box-shadow:0 4px 18px rgba(0,0,0,.18);overflow:hidden;}
  .menu-page > *{position:absolute;margin:0;}
  .heading{font-family:"Teko",sans-serif;font-weight:600;text-transform:uppercase;letter-spacing:.5px;line-height:1;margin:0;}
  .heading--main{font-size:44px;}
  .heading--sub{font-size:21px;}
  sup{font-size:9px;vertical-align:top;position:relative;top:2px;margin-left:4px;}
  .note{font-style:italic;font-size:13px;}
  .item{white-space:nowrap;}
  .price-list{margin:0;padding:0;list-style:none;font-size:19px;line-height:1.3;}
  .price-list li{display:flex;justify-content:space-between;gap:14px;white-space:nowrap;}
  .section-note{font-style:italic;font-size:13px;margin:0 0 4px;}

  /* breakfast */
  .breakfast-title{left:0;right:0;top:18px;text-align:center;}
  .breakfast-intro{left:0;right:0;top:66px;text-align:center;font-size:14px;}
  .breakfast-item{font-size:14px;}

  /* soul food */
  .soul-title{left:0;right:0;top:180px;text-align:center;}
  .soul-intro{left:0;right:0;top:228px;text-align:center;font-size:16px;}
  .soul-note{left:0;right:0;top:252px;text-align:center;}
  .entrees-title{left:70px;top:290px;}
  .entrees-list{left:70px;top:312px;padding-left:22px;font-size:14px;line-height:1.2;}
  .soul-divider{left:500px;top:290px;width:1px;height:120px;background:var(--rule);}
  .sides-title{left:560px;top:288px;}
  .sides-list{left:560px;top:310px;padding:0;list-style:none;font-size:10px;line-height:1.15;}

  /* lunch & dinner */
  .lunch-title{left:60px;top:448px;white-space:nowrap;}
  .burgers{left:450px;top:440px;width:260px;}
  .salads{left:40px;top:520px;width:270px;}
  .seafood{left:500px;top:560px;width:210px;}
  .strips{left:290px;top:630px;width:200px;}
  .chicken{left:40px;top:650px;width:220px;}
  .extra-sides{left:290px;top:760px;width:240px;}
  .ribs{left:40px;top:800px;width:200px;}
  .strips-table{width:100%;border-collapse:collapse;font-size:19px;}
  .strips-table td{padding:0;line-height:1.3;white-space:nowrap;}
  .sides-header{white-space:nowrap;}
  .sides-prices{font-family:"Open Sans",sans-serif;font-size:12px;font-weight:400;text-transform:none;letter-spacing:0;margin-left:6px;}
  .sides-grid{display:grid;grid-template-columns:1fr 1fr;font-size:19px;line-height:1.3;margin-top:4px;white-space:nowrap;}
  .brand{left:550px;top:700px;width:170px;text-align:center;font-family:"Teko",sans-serif;font-weight:600;font-size:36px;line-height:.95;text-transform:uppercase;color:var(--ink);}
</style>
</head>
<body>
<main class="menu-page">

  <h2 class="heading heading--main breakfast-title">Breakfast</h2>
  <p class="breakfast-intro">Plates at $4.<sup>99</sup> or purchase individually</p>
  <p class="item breakfast-item" style="left:510px;top:64px">Baked Ham<sup>$1.99</sup></p>
  <p class="item breakfast-item" style="left:350px;top:92px">Bacon<sup>$1.99</sup></p>
  <p class="item breakfast-item" style="left:520px;top:92px">Sandwiches<sup>$2.99</sup></p>
  <p class="item breakfast-item" style="left:170px;top:112px">Hashbrowns<sup>$1.99</sup></p>
  <p class="item breakfast-item" style="left:360px;top:116px">Pan Cake<sup>$1.99</sup></p>
  <p class="item breakfast-item" style="left:40px;top:132px">Grits<sup>$1.99</sup></p>
  <p class="item breakfast-item" style="left:180px;top:137px">Biscuits<sup>$1.99</sup></p>
  <p class="item breakfast-item" style="left:390px;top:139px">Smoked Link Sausage<sup>$1.99</sup></p>
  <p class="item breakfast-item" style="left:40px;top:157px">Eggs<sup>$1.99</sup></p>
  <p class="item breakfast-item" style="left:150px;top:160px">Sausage Patties<sup>$1.99</sup></p>

  <h2 class="heading heading--main soul-title">Soul Food</h2>
  <p class="soul-intro">Order from the Menu or create a plate from the line for only $7.<sup>99</sup></p>
  <p class="note soul-note">Plate consist of an Entrée or a meat, 2 sides, a bread and drink of the day</p>
  <h3 class="heading heading--sub entrees-title">Entrees</h3>
  <ol class="entrees-list">
    <li>Red beans with rice and sausage</li>
    <li>Beef tips with rice.</li>
    <li>Turkey Necks</li>
    <li>Fried \ Baked chicken.</li>
    <li>Spaghetti</li>
    <li>Stuffed bell pepper (Shrimp, Crab and sausage)</li>
    <li>Chicken on a stick</li>
  </ol>
  <div class="soul-divider"></div>
  <h3 class="heading heading--sub sides-title">Sides</h3>
  <ul class="sides-list">
    <li>Rice</li><li>Mac N Cheese</li><li>Collard Greens</li><li>String Beans</li><li>BBQ red beans</li><li>Mash Potatoes</li><li>Corn Bread</li><li>Green Beans</li><li>Corn</li>
  </ul>

  <h2 class="heading heading--main lunch-title">Lunch &amp; Dinner</h2>

  <section class="burgers">
    <h3 class="heading heading--sub">Burgers</h3>
    <ul class="price-list">
      <li><span>Classic Burger</span><sup>$5.00</sup></li>
      <li><span>Classic Cheeseburger</span><sup>$6.00</sup></li>
      <li><span>Bacon Cheeseburger</span><sup>$7.00</sup></li>
    </ul>
  </section>

  <section class="salads">
    <h3 class="heading heading--sub">Salads</h3>
    <ul class="price-list">
      <li><span>Chef Salad</span><sup>$7.00</sup></li>
      <li><span>Grilled Chicken Salad</span><sup>$7.50</sup></li>
      <li><span>Popcorn Chicken Salad</span><sup>$7.50</sup></li>
    </ul>
  </section>

  <section class="seafood">
    <h3 class="heading heading--sub">Seafood</h3>
    <p class="section-note">Served with 2 sides</p>
    <ul class="price-list">
      <li><span>2 pc. Fried Fish</span><sup>$8.99</sup></li>
      <li><span>6 pc. Shrimp</span><sup>$6.99</sup></li>
      <li><span>12 pc. Shrimp</span><sup>$11.99</sup></li>
    </ul>
  </section>

  <section class="strips">
    <h3 class="heading heading--sub">Strips</h3>
    <p class="section-note">Served with 2 sides</p>
    <table class="strips-table">
      <tr><td>3 pc.<sup>$3.95</sup></td><td>Meal<sup>$5.99</sup></td></tr>
      <tr><td>6 pc.<sup>$7.00</sup></td><td>Meal<sup>$8.99</sup></td></tr>
      <tr><td>9 pc.<sup>$10.99</sup></td><td>Meal<sup>$12.99</sup></td></tr>
    </table>
  </section>

  <section class="chicken">
    <h3 class="heading heading--sub">Fried Chicken</h3>
    <p class="section-note">Served with 2 sides</p>
    <ul class="price-list">
      <li><span>2 pc. White</span><sup>$6.99</sup></li>
      <li><span>2 pc. Dark</span><sup>$4.99</sup></li>
    </ul>
  </section>

  <section class="extra-sides">
    <h3 class="heading heading--sub sides-header">Sides<span class="sides-prices">Individual<sup>$2.00</sup> &nbsp; Large<sup>$4.00</sup></span></h3>
    <div class="sides-grid">
      <span>Okra</span><span>Broccoli</span>
      <span>Fries</span><span>Side Salad</span>
    </div>
  </section>

  <section class="ribs">
    <h3 class="heading heading--sub">Ribs Day!</h3>
    <ul class="price-list">
      <li><span>Full Rack</span><sup>$16.99</sup></li>
      <li><span>Half Rack</span><sup>$8.99</sup></li>
    </ul>
  </section>

  <p class="brand">Juniper<br>Table<br>Restaurant</p>
</main>
</body>
</html>
```